Vantor Glide - Stock Certificate

We need a custom designed stock certificate that represents the look of our company logo but also have a cool look compared to a standard stock certificate. We thinking we want the logo in gold. Our website is https://www.vantorglideusa.example.

We are wanting the certificate to look very professional and really cool, we have sales agents that work for the company and we are creating a program by which the sales agents can gain ownership in the company. So the certificates need to have a very cool appeal and that provides a sense of pride in owning "Units" in Vantor Glide.
Updates

Reason: Extending so other board members can vote as well, thank you all!

Target Market(s)

Stock/Shareholders

Industry/Entity Type

It Company

Font styles to use
Script

Requirements
Must have
• Must look like a stock certificate, must use our logo which the psd file for it was attached.
Nice to have
• Nice to have the logo in gold

```html
<!DOCTYPE html>
<html lang="en">
<head>
<meta charset="UTF-8">
<title>Vantor Glide – Stock Certificate</title>
<link href="https://fonts.googleapis.com/css2?family=Stardos+Stencil:wght@700&family=Dancing+Script:wght@400&family=Jost:wght@400&family=Questrial&display=swap" rel="stylesheet">
<style>
  :root {
    --paper: #ffffff;
    --ink: #000000;
    --rule: #9a9a9a;
    --mark-gold: #d9a021;
    --frame-gold: #c9962a;
  }
  html, body {
    margin: 0;
    padding: 0;
    width: 1200px;
    height: 1000px;
    overflow: hidden;
    background: var(--paper);
  }
  .certificate {
    position: relative;
    width: 1200px;
    height: 1000px;
    background: var(--paper);
    color: var(--ink);
  }
  .certificate__frame {
    position: absolute;
    inset: 22px;
    border: 3px solid var(--frame-gold);
    pointer-events: none;
  }
  .certificate__frame::after {
    content: "";
    position: absolute;
    inset: 8px;
    border: 1px solid var(--frame-gold);
  }
  .certificate__title {
    position: absolute;
    top: 72px;
    left: 0;
    width: 1224px;
    margin: 0;
    text-align: center;
    font-family: "Stardos Stencil", "Impact", sans-serif;
    font-weight: 700;
    font-size: 46px;
    letter-spacing: 5px;
    line-height: 1;
    transform: scaleX(1.23);
    transform-origin: 612px 0;
  }
  .certificate__statement {
    position: absolute;
    top: 216px;
    left: 0;
    width: 1192px;
    margin: 0;
    text-align: center;
    font-family: "Dancing Script", cursive;
    font-size: 50px;
    line-height: 62px;
  }
  .certificate__holder {
    text-decoration: underline;
    text-decoration-thickness: 2px;
    text-underline-offset: 6px;
  }
  .certificate__holder::before { content: "\00a0"; }
  .company-mark {
    position: absolute;
    top: 522px;
    left: 0;
    width: 1212px;
    display: flex;
    flex-direction: column;
    align-items: center;
    gap: 14px;
  }
  .company-mark__dot {
    width: 110px;
    height: 110px;
    border-radius: 50%;
    background: var(--mark-gold);
  }
  .company-mark__name {
    font-family: "Dancing Script", cursive;
    font-size: 32px;
    line-height: 1;
    color: var(--mark-gold);
  }
  .issue-row {
    position: absolute;
    top: 762px;
    left: 258px;
    display: flex;
    align-items: flex-end;
    font-family: "Questrial", sans-serif;
    font-size: 26px;
    line-height: 1;
    -webkit-text-stroke: 0.6px var(--ink);
  }
  .issue-row__label { display: inline-block; white-space: nowrap; }
  .issue-row__label--date { width: 87px; letter-spacing: 1.5px; }
  .issue-row__label--place { width: 35px; letter-spacing: 1px; }
  .issue-row__blank {
    display: inline-block;
    width: 262px;
    height: 0;
    border-bottom: 1px solid var(--rule);
    margin-bottom: -2px;
  }
  .signatures {
    position: absolute;
    top: 875px;
    left: 343px;
    display: flex;
    gap: 34px;
  }
  .signature {
    width: 264px;
    border-top: 1px solid var(--rule);
    text-align: center;
    font-family: "Jost", sans-serif;
    font-size: 23px;
    line-height: 1;
    padding-top: 8px;
  }
</style>
</head>
<body>
  <main class="certificate">
    <div class="certificate__frame"></div>

    <h1 class="certificate__title">STOCK CERTIFICATE</h1>

    <p class="certificate__statement">
      This certifies that<br>
      <span class="certificate__holder">Vantor Glide</span> is&nbsp; the owner of<br>
      the fully paid and non-assessable<br>
      shares of stock.
    </p>

    <div class="company-mark">
      <div class="company-mark__dot"></div>
      <span class="company-mark__name">Vantor Glide</span>
    </div>

    <div class="issue-row">
      <span class="issue-row__label issue-row__label--date">Date:</span>
      <span class="issue-row__blank"></span>
      <span class="issue-row__label issue-row__label--place">At</span>
      <span class="issue-row__blank"></span>
    </div>

    <div class="signatures">
      <div class="signature">President</div>
      <div class="signature">Secretary</div>
    </div>
  </main>
</body>
</html>
```